NEW Household Invention Needs a Package Design!

We need a 'retail' package design for a new product invented for the household kitchen market. Brimloft has developed a reusable food storage system that can be tailored to an individual's needs and have a sustainable impact on their ability to make good dietary decisions, while helping save the planet. We would like to see designs that use the brand's branding guidelines and logo. The final design should communicate the key features of the product (patented customizable modular system, fill lines, collapsible functionality and sustainable materials), as well as, all other notable aspects (Microwave/Dishwasher Safe, Leakproof, 100% BPA Free, Donates 1% of purchase price, etc.). It's important that the benefits of the product are well highlighted (More variety to better balance nutrition, More easily stored in bag, kitchen cabinet or drawer and Ends waste)
Updates

Hi All, we are looking for a package design for retail, something that will be on a shelf in our product category.

Target Market(s)

Health conscious men and women who have a passion for nutrition & social responsibility, operate a lifestyle on-the-go and monitor their spending by preparing meals at home.

Industry/Entity Type

Food Tech, Consumer Products, Health & Wellness

Font styles to use
Other font styles liked:
• See Brand Guidelines

Requirements
Must have
• Follow brand guidelines: https://guidelines.quorvadesign.example/brimloft/guidelines/

```html
<!DOCTYPE html>
<html lang="en">
<head>
<meta charset="utf-8">
<title>Brimloft Reusable Food Storage – Package Front</title>
<link rel="stylesheet" href="https://fonts.googleapis.com/css2?family=Poppins:wght@500;600&family=Barlow+Semi+Condensed:wght@400;500&display=swap">
<style>
  :root {
    --stage: #4f92ad;
    --panel: #f4f8fa;
    --panel-shade: #e3ecf1;
    --brand-blue: #2b8fc4;
    --deep-teal: #1c6785;
    --product-blue: #8cc4e6;
    --product-light: #cfe6f4;
    --ink: #1f2a30;
    --muted: #4a555b;
    --divider: #3b4347;
  }
  * { box-sizing: border-box; margin: 0; padding: 0; }
  html, body { width: 1200px; height: 833px; overflow: hidden; }
  body { background: var(--stage); position: relative; }

  .package-front {
    position: absolute; left: 350px; top: 26px;
    width: 500px; height: 780px;
    background: linear-gradient(160deg, #ffffff 0%, var(--panel) 55%, var(--panel-shade) 100%);
    overflow: hidden;
    box-shadow: 0 18px 40px rgba(20, 50, 65, .35);
  }
  .texture {
    position: absolute; inset: 0;
    background: linear-gradient(180deg, rgba(220,235,243,.5), rgba(255,255,255,0) 60%, rgba(214,228,236,.6));
  }
  .brand-name {
    position: absolute; left: 38px; top: 88px;
    font-family: "Poppins", sans-serif; font-weight: 600;
    font-size: 44px; color: var(--brand-blue); letter-spacing: -0.5px;
  }
  .headline {
    position: absolute; left: 38px; top: 262px;
    font-family: "Poppins", sans-serif; font-weight: 600;
    color: var(--brand-blue); line-height: 1.05;
  }
  .headline .lead { display: block; font-size: 27px; }
  .headline .main { display: block; font-size: 38px; letter-spacing: -0.5px; }
  .feature-card {
    position: absolute; left: 32px; top: 368px;
    width: 200px; height: 118px;
    background: #fff; border-radius: 8px;
    box-shadow: 0 4px 10px rgba(30, 60, 80, .25);
    padding: 10px 8px;
    font-family: "Barlow Semi Condensed", sans-serif; font-weight: 500;
    font-size: 16px; line-height: 1.38; color: var(--ink);
  }
  .product-visual { position: absolute; left: 270px; top: 100px; width: 230px; height: 520px; }

  .benefits {
    position: absolute; left: 30px; top: 556px;
    display: flex; align-items: flex-start;
  }
  .benefit {
    display: flex; flex-direction: column; align-items: center;
    font-family: "Poppins", sans-serif; font-size: 7.5px; line-height: 1.3;
    color: var(--ink); text-align: center;
  }
  .benefit .icon { width: 46px; height: 54px; border-radius: 8px; background: #d9e1e5; margin-bottom: 14px; }
  .benefit-divider { width: 1px; height: 80px; background: var(--divider); margin: 0 16px; }

  .spec-row {
    position: absolute; left: 32px; right: 20px; top: 728px;
    display: flex; align-items: center; justify-content: space-between;
    font-family: "Barlow Semi Condensed", sans-serif; font-size: 12.5px; color: var(--muted);
  }
  .spec-row .sep { width: 1px; height: 18px; background: var(--divider); }
</style>
</head>
<body>
  <main class="package-front">
    <div class="texture" role="img" aria-label="Faint hexagon honeycomb pattern"></div>

    <div class="brand-name">Brimloft</div>

    <h1 class="headline">
      <span class="lead">Reusable</span>
      <span class="main">food storage</span>
    </h1>

    <p class="feature-card">patented customizable modular system, fill lines, collapsible functionality and sustainable materials</p>

    <svg class="product-visual" viewBox="0 0 230 520" role="img" aria-label="Photo of collapsible blue food containers with clear lids and a fork on a blue surface">
      <defs>
        <linearGradient id="productFill" x1="0" y1="0" x2="1" y2="1">
          <stop offset="0" stop-color="var(--product-light)"/>
          <stop offset="1" stop-color="var(--product-blue)"/>
        </linearGradient>
      </defs>
      <path d="M230 60 C150 40 60 120 30 240 C5 340 70 470 190 500 L230 510 Z" fill="url(#productFill)"/>
      <path d="M230 40 C200 10 160 20 130 60 C80 110 30 170 16 260 C4 350 60 440 150 480 C180 495 210 490 230 470"
            fill="none" stroke="var(--deep-teal)" stroke-width="3"/>
    </svg>

    <div class="benefits">
      <div class="benefit">
        <div class="icon" role="img" aria-label="Line drawing of a backpack"></div>
        <span>More easily<br>stored in bag</span>
      </div>
      <div class="benefit-divider"></div>
      <div class="benefit">
        <div class="icon" role="img" aria-label="Line drawing of an avocado"></div>
        <span>More variety to<br>better balance nutrition</span>
      </div>
      <div class="benefit-divider"></div>
      <div class="benefit">
        <div class="icon" role="img" aria-label="Drawing of a kitchen cabinet"></div>
        <span>kitchen cabinet or drawer<br>and Ends waste</span>
      </div>
    </div>

    <div class="spec-row">
      <span>Microwave/Dishwasher Safe</span><span class="sep"></span>
      <span>Leakproof</span><span class="sep"></span>
      <span>100% BPA Free</span><span class="sep"></span>
      <span>Donates 1% of purchase price</span>
    </div>
  </main>
</body>
</html>
```